TUSK Township Union for Stray Kinship

TUSK SCS PET OWNERS WITH VACCINATIONS, MICROCHIP, Spay & NEUTER, TRANSPORTATION FOR PET OWNERS THAT ARE ELDERLY OR MOBILITY CHALLENGED, PET SITTING, PET GROOMING, EDUCATION, adoption counseling, grief counseling, in-home evaluations, feral trap and release, public speaking on education of pet ownership, seminars, meetings and outreach. TUSK depends 100% on donations. I need the webpage to be able to link up to my DonaPay account for donations. Serving the greater Houston area.

Reason: My dog of 15 yrs is dying.

Industry/Entity Type

Pet

```html
<!DOCTYPE html>
<html lang="en">
<head>
<meta charset="utf-8">
<title>TUSK – Township Union for Stray Kinship</title>
<link href="https://fonts.googleapis.com/css2?family=Roboto+Slab:wght@400;700&family=Roboto+Condensed:wght@300;400&display=swap" rel="stylesheet">
<style>
:root{
  --topbar:#6a4824;
  --beige:#e4be88;
  --band:#6f4e28;
  --dark:#2f1d0c;
  --banner:#3a2411;
  --orange:#d77e10;
  --orange-hi:#e38c1a;
  --cream:#f7ecd9;
  --white:#ffffff;
  --ink:#2b2119;
  --muted:#4a4038;
}
*{margin:0;padding:0;box-sizing:border-box}
html,body{width:720px;height:1200px;overflow:hidden}
body{position:relative;background:var(--beige);font-family:"Roboto Slab",Georgia,serif;color:var(--ink)}
.abs{position:absolute}
.topbar{left:0;top:0;width:720px;height:24px;background:var(--topbar)}
.topbar-contact{right:107px;top:7px;font-family:"Roboto Condensed",Arial,sans-serif;font-size:8px;color:var(--white)}
.hero-area{left:0;top:24px;width:720px;height:338px;background:linear-gradient(180deg,#e8c690,#dfb67e)}
.logo{left:97px;top:36px;font-size:28px;font-weight:700;color:#3a2210;letter-spacing:1px}
.nav{left:196px;top:37px;display:flex;height:37px;align-items:center;font-size:10px;color:var(--ink)}
.nav a{color:inherit;text-decoration:none;margin-right:26px}
.nav .active{background:var(--orange);color:var(--white);height:37px;line-height:37px;padding:0 14px;margin-right:16px}
.search{left:512px;top:47px;width:110px;height:15px;background:#f1d6a6;border-radius:2px;font-size:6px;color:#8f7453;padding:4px 4px;font-family:"Roboto Condensed",Arial,sans-serif}
.slide{left:97px;top:76px;width:365px;height:196px;background:linear-gradient(160deg,#b98d5a,#8c6a48 45%,#5d4b3c);box-shadow:0 6px 6px -3px rgba(60,35,10,.45)}
.slide-caption{left:0;bottom:0;width:100%;height:28px;background:rgba(30,20,10,.45);color:var(--white);font-size:9px;line-height:28px;padding-left:30px;font-family:"Roboto Condensed",Arial,sans-serif}
.slide-caption svg{position:absolute;top:9px}
.quote-panel{left:471px;top:76px;width:151px;height:196px;background:linear-gradient(180deg,#6d6a68,#3a3b3d 55%,#242628)}
.quote-text{left:8px;top:112px;width:138px;text-align:center;color:var(--white);font-family:"Roboto Condensed",Arial,sans-serif;font-weight:300;font-size:9.3px;line-height:14px}
.quote-by{left:60px;top:184px;font-size:4.5px;color:#d8d8d8;font-family:"Roboto Condensed",Arial,sans-serif}
.dots{left:120px;top:186px;display:flex;gap:4px}
.dots i{width:4px;height:4px;border-radius:50%;background:#555}
.dots i:first-child{background:#fff}
.support-tab{left:686px;top:118px;width:34px;height:104px;background:#5a3a17;border:1px solid #8b6333;border-right:none;border-radius:3px 0 0 3px}
.support-tab span{position:absolute;left:50%;top:50%;transform:translate(-50%,-50%) rotate(-90deg);white-space:nowrap;color:var(--white);font-size:10px;font-weight:700}
.banner{left:96px;width:526px;background:var(--banner);border-radius:3px}
.banner-transport{top:292px;height:70px}
.banner-transport h2{position:absolute;left:72px;top:13px;font-size:17px;line-height:20px;color:var(--white);font-weight:700}
.btn{background:var(--orange);color:var(--white);display:flex;align-items:center;justify-content:center;border-radius:2px}
.btn-join{left:528px;top:308px;width:89px;height:38px;font-size:11px;font-weight:700}
.band{left:0;width:720px;background:var(--band)}
.band-provide{top:362px;height:161px}
.section-title{width:720px;text-align:center;font-size:12.5px;font-weight:700}
.provide-title{top:384px;color:var(--white)}
.service-photo{width:88px;height:88px;border-radius:50%;border:2px solid #f3e5cf}
.service-label{font-size:9.5px;color:var(--white)}
.btn-small{height:18px;padding:0 7px;font-size:7.3px}
.white-area{left:0;top:523px;width:720px;height:327px;background:var(--white)}
.do-title{top:538px;color:var(--ink)}
.do-card{width:127px;height:80px;border:1px solid #d9d9d9;border-radius:2px}
.do-heading{width:160px;text-align:center;font-size:9.5px;color:var(--ink)}
.do-text{width:160px;text-align:center;font-size:7.2px;line-height:12.7px;color:var(--muted);font-family:"Roboto Condensed",Arial,sans-serif}
.banner-donate{top:780px;height:70px;z-index:2}
.banner-donate h2{position:absolute;left:18px;top:24px;font-size:17px;color:var(--white);font-weight:700}
.btn-donate{left:449px;top:799px;width:168px;height:38px;z-index:3;gap:12px}
.btn-donate .pay-name{font-size:17px;font-weight:700}
.btn-donate .pay-label{font-size:10px;font-weight:700}
.band-lower{top:850px;height:278px;background:linear-gradient(180deg,#6b4a25,#5c3f1f)}
.lower-title{font-size:12.5px;font-weight:700;color:var(--white)}
.gallery{left:106px;top:908px;width:254px;height:175px;border:2px solid #d7b58a;background:linear-gradient(120deg,#6a4120,#8b8077 45%,#e4e0dc 70%,#5e5048)}
.thumb{top:122px;width:60px;height:46px;border:2px solid #d7b58a}
.news-photo{left:373px;width:101px;height:63px;background:linear-gradient(120deg,#c9a88c,#f0e3d6 50%,#9a8470)}
.news-date{left:0;bottom:0;width:28px;height:26px;background:var(--orange);color:var(--white);font-size:7px;font-weight:700;line-height:8px;text-align:center;padding-top:5px}
.news-text{left:481px;width:140px;font-size:7.1px;line-height:12.7px;color:#f4e6d2;font-family:"Roboto Condensed",Arial,sans-serif}
.news-text b{color:var(--white);font-family:"Roboto Slab",Georgia,serif;font-size:6.8px}
.news-text a{color:var(--orange-hi);text-decoration:none}
.btn-view{height:18px;font-size:7.3px}
.footer{left:0;top:1128px;width:720px;height:72px;background:var(--dark)}
.footer-links{left:97px;top:21px;font-size:7.5px;color:var(--white);font-family:"Roboto Condensed",Arial,sans-serif;word-spacing:2px}
.footer-copy{left:97px;top:40px;font-size:7.5px;color:var(--white);font-family:"Roboto Condensed",Arial,sans-serif}
.social{top:27px;font-size:8px;font-weight:700;color:var(--white)}
</style>
</head>
<body>

<header>
  <div class="abs topbar"></div>
  <div class="abs topbar-contact">Call Now : 1-800-555-0147 &nbsp;| &nbsp;Login</div>
  <div class="abs hero-area"></div>
  <div class="abs logo">TUSK</div>
  <nav class="abs nav">
    <a class="active" href="#">Home</a>
    <a href="#">About Us</a>
    <a href="#">Services</a>
    <a href="#">FAQ's</a>
    <a href="#">Contact Us</a>
  </nav>
  <div class="abs search">Search</div>
</header>

<section>
  <div class="abs slide" role="img" aria-label="Photo of two cats peeking out of a cardboard box">
    <div class="abs slide-caption">
      <svg style="left:10px" width="6" height="10" viewBox="0 0 6 10"><path d="M5 1 1 5l4 4" stroke="#fff" stroke-width="1.4" fill="none"/></svg>
      Neque porro quisquam est qui dolorem ipsum quia dolor sit amet, ...
      <svg style="right:10px" width="6" height="10" viewBox="0 0 6 10"><path d="m1 1 4 4-4 4" stroke="#fff" stroke-width="1.4" fill="none"/></svg>
    </div>
  </div>
  <div class="abs quote-panel" role="img" aria-label="Photo of a dark puppy looking up">
    <p class="abs quote-text">“ The greatest pleasure of a dog is that you may make a fool of yourself with him, and not only will he not scold you, but he will make a fool of himself, too. ”</p>
    <span class="abs quote-by">- Edwin Marlow</span>
    <div class="abs dots"><i></i><i></i><i></i><i></i></div>
  </div>
  <div class="abs support-tab"><span>Customer Support</span></div>
</section>

<section class="abs banner banner-transport">
  <svg class="abs" style="left:20px;top:12px" width="42" height="46" viewBox="0 0 42 46">
    <circle cx="12" cy="5" r="4" fill="#d77e10"/>
    <path d="M12 11v14h12l6 12 5-2" stroke="#d77e10" stroke-width="4" fill="none" stroke-linejoin="round"/>
    <path d="M12 17h9" stroke="#d77e10" stroke-width="3"/>
    <path d="M8 21a11 11 0 1 0 16 14" stroke="#d77e10" stroke-width="3" fill="none"/>
  </svg>
  <h2>We give transportation to pet owners<br>who are elderly or mobility challenged</h2>
</section>
<div class="abs btn btn-join">Join Us</div>

<section>
  <div class="abs band band-provide"></div>
  <h2 class="abs section-title provide-title">What We Provide ?</h2>

  <div class="abs service-photo" style="left:97px;top:416px;background:linear-gradient(135deg,#e9a25c,#d98040 50%,#7fa6a6)" role="img" aria-label="Photo of a ginger cat at the vet"></div>
  <span class="abs service-label" style="left:196px;top:456px">Vaccinations</span>
  <div class="abs btn btn-small" style="left:196px;top:472px">Read More</div>

  <div class="abs service-photo" style="left:282px;top:416px;background:linear-gradient(135deg,#c9d6e6,#8aa4c2 50%,#5e6b78)" role="img" aria-label="Photo of a pet microchip held in gloved fingers"></div>
  <span class="abs service-label" style="left:381px;top:456px">Microchip</span>
  <div class="abs btn btn-small" style="left:381px;top:472px">Read More</div>

  <div class="abs service-photo" style="left:451px;top:417px;background:radial-gradient(circle at 50% 45%,#4a3a2c,#9b8a7a 55%,#e6e6e8)" role="img" aria-label="Photo of a small terrier dog"></div>
  <span class="abs service-label" style="left:553px;top:456px">Spay &amp; Neuter</span>
  <div class="abs btn btn-small" style="left:554px;top:472px">Read More</div>
</section>

<section>
  <div class="abs white-area"></div>
  <h2 class="abs section-title do-title">What We Do ?</h2>

  <div class="abs do-card" style="left:124px;top:580px;background:linear-gradient(180deg,#4f8a2c,#3d6f20);border:none" role="img" aria-label="Photo of a beagle puppy sitting on grass"></div>
  <h3 class="abs do-heading" style="left:101px;top:670px;font-weight:400">Pet Sitting</h3>
  <p class="abs do-text" style="left:98px;top:699px">Lorem Ipsum is simply dummy text of the printing and typesetting industry. Lorem Ipsum has been the industry's standard dummy text ever since the 1500s</p>

  <div class="abs do-card" style="left:321px;top:580px;background:radial-gradient(circle at 55% 60%,#f2b7cc,#fbe6ee 45%,#fff 70%)" role="img" aria-label="Photo of a small dog wrapped in a pink towel"></div>
  <h3 class="abs do-heading" style="left:301px;top:670px;font-weight:400">Pet Grooming</h3>
  <p class="abs do-text" style="left:297px;top:699px">Lorem Ipsum is simply dummy text of the printing and typesetting industry. Lorem Ipsum has been the industry's standard dummy text ever since the 1500s</p>

  <div class="abs do-card" style="left:500px;top:580px;background:radial-gradient(circle at 50% 55%,#8a7a6a,#e9e4df 50%,#fff 70%)" role="img" aria-label="Photo of two small dogs in graduation caps"></div>
  <h3 class="abs do-heading" style="left:486px;top:670px;font-weight:400">Education</h3>
  <p class="abs do-text" style="left:481px;top:699px">Lorem Ipsum is simply dummy text of the printing and typesetting industry. Lorem Ipsum has been the industry's standard dummy text ever since the 1500s</p>
</section>

<section class="abs banner banner-donate">
  <h2>TUSK depends 100% on donations</h2>
</section>
<a class="abs btn btn-donate" href="#"><span class="pay-name">DonaPay</span><span class="pay-label">Donate now</span></a>

<section>
  <div class="abs band band-lower"></div>
  <h2 class="abs lower-title" style="left:107px;top:880px">Photo Gallery</h2>
  <div class="abs gallery" role="img" aria-label="Photo of a long-haired cat">
    <svg class="abs" style="left:10px;top:78px" width="10" height="16" viewBox="0 0 10 16"><path d="M8 2 2 8l6 6" stroke="#fff" stroke-width="2.4" fill="none"/></svg>
    <svg class="abs" style="right:10px;top:78px" width="10" height="16" viewBox="0 0 10 16"><path d="m2 2 6 6-6 6" stroke="#fff" stroke-width="2.4" fill="none"/></svg>
    <div class="abs thumb" style="left:19px;background:linear-gradient(135deg,#8a8a8a,#ddd 50%,#333)" role="img" aria-label="Thumbnail photo of a black and white cat"></div>
    <div class="abs thumb" style="left:95px;background:linear-gradient(135deg,#3a6a6a,#b09050 50%,#2a3a2a)" role="img" aria-label="Thumbnail photo of a dog"></div>
    <div class="abs thumb" style="left:171px;background:linear-gradient(135deg,#5a3a22,#e8e4e0 55%,#3a2a1c)" role="img" aria-label="Thumbnail photo of a fluffy cat"></div>
  </div>
  <div class="abs btn btn-view" style="left:285px;top:1096px;width:75px">View More Photos</div>

  <h2 class="abs lower-title" style="left:373px;top:880px">Latest News</h2>

  <div class="abs news-photo" style="top:908px" role="img" aria-label="Photo of a woman hugging her dog">
    <div class="abs news-date">AUG<br>2014</div>
  </div>
  <p class="abs news-text" style="top:906px"><b>Lorem Ipsum is simply dummy text of the printing and typesetting industry.</b> Lorem Ipsum has been the industry's standard dummy text ever since the 1500s Lorem Ipsum is simply dummy text of the printing <a href="#">...Read More</a></p>

  <div class="abs news-photo" style="top:1014px;background:linear-gradient(120deg,#e8e0d6,#8a6a50 50%,#3a2a22)" role="img" aria-label="Photo of a child and a woman holding a puppy">
    <div class="abs news-date">AUG<br>2014</div>
  </div>
  <p class="abs news-text" style="top:1011px"><b>Lorem Ipsum is simply dummy text of the printing and typesetting industry.</b> Lorem Ipsum has been the industry's standard dummy text ever since the 1500s Lorem Ipsum is simply dummy text of the printing <a href="#">...Read More</a></p>

  <div class="abs btn btn-view" style="left:547px;top:1096px;width:76px">View More News</div>
</section>

<footer class="abs footer">
  <div class="abs footer-links">Home &nbsp; | &nbsp; About Us &nbsp; | &nbsp; Services &nbsp; | &nbsp; FAQ's &nbsp; | &nbsp; Contact Us</div>
  <div class="abs footer-copy">© 2014 Company Name ,All Rights Reserved</div>
  <span class="abs social" style="left:560px">Chirp</span>
  <span class="abs social" style="left:592px">Facelink</span>
</footer>

</body>
</html>
```